Xmas banner Lathermoss handmade skincare

We need a xmas sale banner for our skincare website and a few different ones for instagram. Our website is www.lathermoss-example.com, you can use any of our products to include in the banner. We also have some nice product group pictures on our instagram.com/lathermoss_example. If you could include a christmassy message for example "its beginning to feel alot like christmas".

Target Market(s)

Women, 18-35, luxury, handmade natural shoppers

Requirements
Must have
• See our site and instagram. You have creative freedom.
Nice to have
• Try incorporating our products in imaginative ways, for example using bath bombs as Christmas tree baubles
Should not have
• Dont send anything if you think it will look out of place.

```html
<!DOCTYPE html>
<html lang="en">
<head>
<meta charset="utf-8">
<title>Lathermoss – Ho Ho Ho Christmas banners</title>
<link rel="stylesheet" href="https://fonts.googleapis.com/css2?family=Josefin+Sans:wght@200;300;400&display=swap">
<style>
  :root {
    --sheet-bg: #f6f6f6;
    --cocoa-light: #8a6660;
    --cocoa: #6b4b45;
    --cocoa-dark: #4f3832;
    --gold: #f7dc0c;
    --label-ink: #111111;
    --logo-ink: #f4ece6;
  }
  html, body {
    margin: 0;
    padding: 0;
    overflow: hidden;
  }
  body {
    width: 1200px;
    height: 1200px;
    background: radial-gradient(circle at 50% 50%, #ffffff 0%, var(--sheet-bg) 70%, #ececec 100%);
    position: relative;
    font-family: "Josefin Sans", sans-serif;
  }
  .banner {
    position: absolute;
    display: block;
  }
  .banner--rectangle { left: 61px; top: 131px; width: 538px; height: 448px; }
  .banner--skyscraper { left: 742px; top: 35px; width: 384px; height: 640px; }
  .banner--leaderboard { left: 16px; top: 905px; width: 1165px; height: 144px; }

  .headline {
    fill: var(--gold);
    font-family: "Josefin Sans", sans-serif;
    font-weight: 400;
    filter: drop-shadow(1px 2px 2px rgba(40, 20, 10, 0.45));
  }
  .rule { fill: var(--gold); }
  .brand-name {
    fill: var(--logo-ink);
    font-family: "Josefin Sans", sans-serif;
    font-weight: 400;
    letter-spacing: 0.12em;
  }
  .size-label {
    position: absolute;
    margin: 0;
    font-family: "Josefin Sans", sans-serif;
    font-weight: 200;
    font-size: 66px;
    color: var(--label-ink);
    line-height: 1;
    transform: translateX(-50%);
    white-space: nowrap;
  }
  .size-label--rectangle { left: 330px; top: 605px; }
  .size-label--skyscraper { left: 934px; top: 700px; }
  .size-label--leaderboard { left: 594px; top: 1070px; }
</style>
</head>
<body>

<svg width="0" height="0" style="position:absolute" aria-hidden="true">
  <defs>
    <radialGradient id="cocoa-glow" cx="0.65" cy="0.3" r="0.9">
      <stop offset="0" stop-color="var(--cocoa-light)"/>
      <stop offset="0.55" stop-color="var(--cocoa)"/>
      <stop offset="1" stop-color="var(--cocoa-dark)"/>
    </radialGradient>
    <radialGradient id="bomb-yellow" cx="0.4" cy="0.35" r="0.7">
      <stop offset="0" stop-color="#fbf27a"/>
      <stop offset="1" stop-color="#e3cf2a"/>
    </radialGradient>
    <radialGradient id="bomb-pink" cx="0.4" cy="0.35" r="0.7">
      <stop offset="0" stop-color="#ee7fb8"/>
      <stop offset="1" stop-color="#c73f86"/>
    </radialGradient>
    <radialGradient id="bomb-blue" cx="0.4" cy="0.35" r="0.7">
      <stop offset="0" stop-color="#86c4f2"/>
      <stop offset="1" stop-color="#3f86d0"/>
    </radialGradient>
  </defs>
</svg>

<!-- 336x280 -->
<svg class="banner banner--rectangle" viewBox="0 0 538 448" role="group" aria-label="Ho ho ho, it's Christmas banner, medium rectangle">
  <rect width="538" height="448" fill="url(#cocoa-glow)" role="img" aria-label="Soft cocoa backdrop with scattered golden bokeh"/>
  <text class="headline" x="43" y="153" font-size="90" text-anchor="middle" dominant-baseline="central" transform="rotate(-30 43 153)">H</text>
  <circle cx="122" cy="122" r="46" fill="url(#bomb-yellow)" role="img" aria-label="Yellow bath bomb photo"/>
  <text class="headline" x="227" y="85" font-size="90" text-anchor="middle" dominant-baseline="central" transform="rotate(-4 227 85)">H</text>
  <circle cx="306" cy="83" r="45" fill="url(#bomb-pink)" role="img" aria-label="Pink bath bomb photo"/>
  <text class="headline" x="417" y="113" font-size="90" text-anchor="middle" dominant-baseline="central" transform="rotate(35 417 113)">H</text>
  <circle cx="483" cy="153" r="42" fill="url(#bomb-blue)" role="img" aria-label="Blue bath bomb photo"/>
  <text class="headline" x="267" y="246" font-size="76" text-anchor="middle">IT<tspan dx="4" dy="-58" font-size="40">’</tspan><tspan dx="4" dy="58">S</tspan></text>
  <text class="headline" x="263" y="331" font-size="82" text-anchor="middle" textLength="404" lengthAdjust="spacingAndGlyphs">CHRISTMAS!</text>
  <rect class="rule" x="0" y="409" width="344" height="8"/>
  <text class="brand-name" x="361" y="415" font-size="19" textLength="158" lengthAdjust="spacingAndGlyphs">LATHERMOSS</text>
</svg>
<p class="size-label size-label--rectangle">336x280</p>

<!-- 240x400 -->
<svg class="banner banner--skyscraper" viewBox="0 0 384 640" role="group" aria-label="Ho ho ho, it's Christmas banner, skyscraper">
  <rect width="384" height="640" fill="url(#cocoa-glow)" role="img" aria-label="Soft cocoa backdrop with scattered golden bokeh"/>
  <text class="headline" x="162" y="101" font-size="82" text-anchor="middle" dominant-baseline="central" transform="rotate(-30 162 101)">H</text>
  <circle cx="230" cy="71" r="40" fill="url(#bomb-yellow)" role="img" aria-label="Yellow bath bomb photo"/>
  <text class="headline" x="46" y="241" font-size="82" text-anchor="middle" dominant-baseline="central" transform="rotate(-25 46 241)">H</text>
  <circle cx="112" cy="215" r="40" fill="url(#bomb-pink)" role="img" aria-label="Pink bath bomb photo"/>
  <text class="headline" x="266" y="257" font-size="82" text-anchor="middle" dominant-baseline="central" transform="rotate(35 266 257)">H</text>
  <circle cx="326" cy="293" r="38" fill="url(#bomb-blue)" role="img" aria-label="Blue bath bomb photo"/>
  <text class="headline" x="186" y="413" font-size="70" text-anchor="middle">IT<tspan dx="4" dy="-54" font-size="36">’</tspan><tspan dx="4" dy="54">S</tspan></text>
  <text class="headline" x="188" y="489" font-size="74" text-anchor="middle" textLength="362" lengthAdjust="spacingAndGlyphs">CHRISTMAS!</text>
  <rect class="rule" x="0" y="605" width="235" height="7"/>
  <text class="brand-name" x="254" y="611" font-size="16" textLength="120" lengthAdjust="spacingAndGlyphs">LATHERMOSS</text>
</svg>
<p class="size-label size-label--skyscraper">240x400</p>

<!-- 728x90 -->
<svg class="banner banner--leaderboard" viewBox="0 0 1165 144" role="group" aria-label="Ho ho ho banner, leaderboard">
  <rect width="1165" height="144" fill="url(#cocoa-glow)" role="img" aria-label="Soft cocoa backdrop with scattered golden bokeh"/>
  <text class="headline" x="136" y="87" font-size="132" text-anchor="middle" dominant-baseline="central" transform="rotate(-8 136 87)">H</text>
  <circle cx="238" cy="65" r="58" fill="url(#bomb-yellow)" role="img" aria-label="Yellow bath bomb photo"/>
  <text class="headline" x="432" y="67" font-size="132" text-anchor="middle" dominant-baseline="central" transform="rotate(-5 432 67)">H</text>
  <circle cx="528" cy="73" r="56" fill="url(#bomb-pink)" role="img" aria-label="Pink bath bomb photo"/>
  <text class="headline" x="720" y="83" font-size="132" text-anchor="middle" dominant-baseline="central" transform="rotate(-8 720 83)">H</text>
  <circle cx="812" cy="65" r="56" fill="url(#bomb-blue)" role="img" aria-label="Blue and green bath bomb photo"/>
  <rect class="rule" x="868" y="110" width="112" height="6"/>
  <text class="brand-name" x="992" y="116" font-size="20" textLength="160" lengthAdjust="spacingAndGlyphs">LATHERMOSS</text>
</svg>
<p class="size-label size-label--leaderboard">728x90</p>

</body>
</html>
```